wardrobe/costume stylist needs good business card for own business

Hi:)

I'm wanting a business card for my company. I am a freelance stylist.

I do wardrobe/costume stylist to TV commercials; Films; Fashion and Lifestyle shoots.

I'd like a design based around my name Rosalind Pember written nicely, maybe a colour? Up to you?!

I've attached a couple of images of business cards I like
.... be creative and have fun!

Thank you :)
Updates

Reason: I was trying to get my new business card ready for before I headed overseas Friday morning but I don't think that was realistic so I'd like to extend the deadline to give time to the project. Thank you

Hi designers:) Thank you for all your designs, I've extended the deadline until Sunday, so there's a bit more time. I've attached 3 pictures of business cards which I quite like, please take a look to see if it can be of help in your process. I like the pale plain or patterned background with dark font and the dark plain or patterned background with the pale font the motifs the feminine fonts the plain fonts I like the idea of playing with a circle or some shape on one side of the card with my name or initials as in the picture I have on my post could you play around with this idea a bit please? Thank you all for the work you've done :) Rosa

Hi I am working overseas til Saturday night sorry for no feedback until I teturn Thanks :) Rosa

Hi designers, Thank you all so much for submitting your designs, I really appreciate your input into my project :) I'm sorry I didn't get to respond to some comments, and give feedback. I didn't back from being away until later than I expected, and the deadline had passed then, so apologies. Thanks to you all again for all your really good designs :) Rosa

Target Market(s)

I am a freelance stylist my target audience is producers, production companies, photographers, directors...

Industry/Entity Type

Business

Requirements
Must have
• Rosalind Pember
Stylist or Wardrobe Stylist

email rosapember@quillnet.co.nz
Mobile 0218846193

(Don't have to use the words 'email' and 'mobile')
Nice to have
• Would like it to be double sided
Like B & W
Like pale colour background with dark font or white font
Like dark colour background with pale font
Should not have
• I would prefer it not to incorporate pictures

```html
<!DOCTYPE html>
<html lang="en">
<head>
<meta charset="utf-8">
<title>Rosalind Pember – Stylist Business Card</title>
<link rel="stylesheet" href="https://fonts.googleapis.com/css2?family=Pinyon+Script&family=Cormorant+Garamond:ital,wght@1,500&display=swap">
<style>
  :root {
    --page-bg: #e9e6e1;
    --card-gold-light: #f1ee9e;
    --card-gold: #dcd66a;
    --card-gold-deep: #c9c15a;
    --ink-black: #161410;
    --card-white: #fbfbf9;
    --gold-text: #c2a52e;
    --ornament-dark: rgba(22, 20, 16, 0.55);
    --card-shadow: 0 14px 30px rgba(0, 0, 0, 0.22);
  }
  * { box-sizing: border-box; margin: 0; padding: 0; }
  html, body {
    width: 1200px;
    height: 900px;
    overflow: hidden;
    background: var(--page-bg);
  }
  .card-set {
    width: 1200px;
    height: 900px;
    display: flex;
    flex-direction: column;
    align-items: center;
    justify-content: center;
    gap: 48px;
  }
  .card {
    position: relative;
    width: 600px;
    height: 343px;
    box-shadow: var(--card-shadow);
    overflow: hidden;
  }
  .card-front {
    background: linear-gradient(120deg, var(--card-gold-light) 0%, var(--card-gold) 55%, var(--card-gold-deep) 100%);
  }
  .ornament {
    position: absolute;
  }
  .ornament-top-right {
    top: 0;
    right: 0;
    width: 190px;
    height: 170px;
    background: radial-gradient(ellipse at 75% 30%, var(--ornament-dark) 0%, rgba(22,20,16,0.25) 45%, rgba(22,20,16,0) 72%);
  }
  .ornament-bottom-left {
    bottom: 0;
    left: 0;
    width: 140px;
    height: 110px;
    background: radial-gradient(ellipse at 30% 65%, var(--ornament-dark) 0%, rgba(22,20,16,0.25) 45%, rgba(22,20,16,0) 72%);
  }
  .name-block {
    position: absolute;
    left: 0;
    right: 0;
    top: 112px;
    text-align: center;
    color: var(--ink-black);
  }
  .client-name {
    font-family: "Pinyon Script", cursive;
    font-weight: 400;
    font-size: 72px;
    line-height: 1;
  }
  .client-role {
    margin-top: 6px;
    padding-left: 150px;
    font-family: "Cormorant Garamond", serif;
    font-style: italic;
    font-size: 20px;
    letter-spacing: 1px;
  }
  .card-back {
    background: var(--card-white);
    display: flex;
    flex-direction: column;
    align-items: center;
    justify-content: center;
    gap: 6px;
    color: var(--gold-text);
    font-family: "Cormorant Garamond", serif;
    font-style: italic;
    font-weight: 500;
  }
  .contact-email {
    font-size: 30px;
    letter-spacing: 3px;
  }
  .contact-phone {
    font-size: 34px;
    letter-spacing: 5px;
  }
</style>
</head>
<body>
  <main class="card-set">
    <section class="card card-front">
      <div class="ornament ornament-top-right" role="img" aria-label="Black baroque flourish ornament in the top right corner"></div>
      <div class="ornament ornament-bottom-left" role="img" aria-label="Black baroque flourish ornament in the bottom left corner"></div>
      <div class="name-block">
        <h1 class="client-name">Rosalind Pember</h1>
        <p class="client-role">stylist</p>
      </div>
    </section>
    <section class="card card-back">
      <p class="contact-email">rosapember@quillnet.co.nz</p>
      <p class="contact-phone">0218846193</p>
    </section>
  </main>
</body>
</html>
```